Civil Engineering Business Card Design

We need a business card design for an Civil Engineering Company located in Naples, Florida. The company name is Dorvel Engineering.
What we do:
Site Evaluation
Review existing site conditions and zoning
Evaluation of potential development options
Evaluation of environmental permitting challenges
Prepare alternative master site development or redevelopment plan
Calculate cost and time lines for site development
Address political, environmental, social, and economic impacts of site development
Site Design
Prepare master site development plans
Zoning, rezoning, and zoning amendments for land use changes
Evaluate zoning and environmental permitting challenges
Value engineer alternative land development design and products
Residential Development
Plat development and design
Homeowner association document development
Single family development ranging from affordable housing to large estate projects
Multi family development ranging from duplexes to large scale condominiums
Amenity facilities such as golf courses, parks and clubhouse sites
Commercial Development
Office site and park designs development plans
Industrial site and park development plans
Shopping center site development design
Hospital site design development
Institutional Development
School design development and redevelopment plans
Park design development and enhancement plans
Downtown redevelopment plans for new and existing structures
Theater and park plan development
Parking garage design development
Governmental administration building design
Design Services
Site development
Environmental assessment
Roadway alignment and development
Surface water management
Drainage design
Water distribution system
Fire service analysis
Sewage collection systems
Sewage pump station and force main design
Cable utility conduit layout
Construction details
Construction documents
Technical specifications
Alternative methods and materials analysis
Services During Construction
Development of bid documents
Solicitation and processing of bids
Cost review and analysis
Construction cost estimating
Onsite construction observation
Coordination of field modifications to address unforeseen site conditions
Assess value engineering design and contract work
Review of pay requests and shop drawings
Review of warranties
Development assessment of onsite and offsite mitigation
Verification of construction completion, close out, and certification
Processing final pay requests and turn over
We want a clean design on a white background. We have a current logo but are not happy with it so changes would be greatly appreciated.
Industry/Entity Type
Construction
Contact Information for Business Card
Dorvel Engineering
Creative Engineering Solutions Through Integrity and Experience
Marcus Dorvel, President
4817 Bracken Loop West
Suite 418C
Naples, FL 34987
239-555-0143-Office, 239-555-0178-Mobile
Marc@DorvelEng.com, www.DorvelEng.com

```html
<!DOCTYPE html>
<html lang="en">
<head>
<meta charset="utf-8">
<title>Dorvel Engineering – Business Card</title>
<link rel="stylesheet" href="https://fonts.googleapis.com/css2?family=Titillium+Web:wght@400;600;700;900&display=swap">
<style>
  :root {
    --stage: #d9d9d9;
    --card-white: #ffffff;
    --card-black: #1c1c1c;
    --orange: #f6a21e;
    --ink: #2a2a2a;
    --muted: #6b6b6b;
    --rule: #bdbdbd;
    --icon-tile: #2f2f2f;
  }
  * { box-sizing: border-box; margin: 0; padding: 0; }
  html, body { width: 1200px; height: 988px; overflow: hidden; }
  body {
    background: var(--stage);
    font-family: "Titillium Web", sans-serif;
    position: relative;
  }
  .card {
    position: absolute;
    left: 220px;
    width: 760px;
    height: 434px;
    border-radius: 4px;
    box-shadow: 0 6px 18px rgba(0,0,0,.18);
  }
  .card--back { top: 40px; background: var(--card-black); }
  .card--front { top: 514px; background: var(--card-white); }

  .brand { position: absolute; display: flex; align-items: center; gap: 18px; }
  .brand__mark { width: 56px; height: 56px; background: var(--orange); }
  .brand__name {
    font-weight: 900; font-size: 46px; line-height: 1;
    color: var(--orange); letter-spacing: .5px;
  }
  .card--back .brand { left: 50%; top: 50%; transform: translate(-50%, -50%); }
  .card--front .brand { left: 62px; top: 92px; }
  .card--front .brand__mark { width: 48px; height: 48px; }
  .card--front .brand__name { font-size: 40px; }

  .top-rule {
    position: absolute; right: 40px; top: 44px;
    width: 300px; height: 1px; background: var(--rule);
  }

  .person { position: absolute; left: 62px; top: 196px; }
  .person__name {
    font-weight: 700; font-size: 24px; color: var(--orange);
    text-transform: uppercase; letter-spacing: .5px; line-height: 1.1;
  }
  .person__title {
    font-size: 12px; color: var(--muted); text-transform: uppercase;
    letter-spacing: 1px; margin-top: 2px;
  }

  .contacts { position: absolute; list-style: none; }
  .contacts--left { left: 62px; top: 262px; width: 300px; }
  .contacts--right { left: 420px; top: 196px; width: 290px; }
  .contact {
    display: flex; align-items: center; gap: 14px;
    height: 42px; border-bottom: 1px solid var(--rule);
    margin-bottom: 10px;
    font-size: 14px; color: var(--ink); letter-spacing: .3px;
  }
  .contact__icon {
    width: 26px; height: 26px; border-radius: 5px;
    background: var(--icon-tile); flex: none;
    display: flex; align-items: center; justify-content: center;
  }
  .contact__icon svg { width: 14px; height: 14px; fill: var(--orange); }
</style>
</head>
<body>

<section class="card card--back" aria-label="Card back">
  <div class="brand">
    <span class="brand__mark"></span>
    <span class="brand__name">Dorvel Engineering</span>
  </div>
</section>

<section class="card card--front" aria-label="Card front">
  <span class="top-rule"></span>

  <div class="brand">
    <span class="brand__mark"></span>
    <span class="brand__name">Dorvel Engineering</span>
  </div>

  <div class="person">
    <p class="person__name">Marcus Dorvel</p>
    <p class="person__title">President</p>
  </div>

  <ul class="contacts contacts--left">
    <li class="contact">
      <span class="contact__icon"><svg viewBox="0 0 24 24"><path d="M6.6 10.8a15.1 15.1 0 0 0 6.6 6.6l2.2-2.2a1 1 0 0 1 1-.25 11.4 11.4 0 0 0 3.6.57 1 1 0 0 1 1 1V20a1 1 0 0 1-1 1A17 17 0 0 1 3 4a1 1 0 0 1 1-1h3.5a1 1 0 0 1 1 1c0 1.25.2 2.45.57 3.6a1 1 0 0 1-.25 1z"/></svg></span>
      239-555-0143
    </li>
    <li class="contact">
      <span class="contact__icon"><svg viewBox="0 0 24 24"><path d="M7 2h10a2 2 0 0 1 2 2v16a2 2 0 0 1-2 2H7a2 2 0 0 1-2-2V4a2 2 0 0 1 2-2zm0 3v13h10V5zm5 14.2a1 1 0 1 0 0 .01z"/></svg></span>
      239-555-0178
    </li>
    <li class="contact">
      <span class="contact__icon"><svg viewBox="0 0 24 24"><path d="M12 2a7 7 0 0 0-7 7c0 5.2 7 13 7 13s7-7.8 7-13a7 7 0 0 0-7-7zm0 9.5A2.5 2.5 0 1 1 12 6.5a2.5 2.5 0 0 1 0 5z"/></svg></span>
      4817 Bracken Loop West, Suite 418C
    </li>
  </ul>

  <ul class="contacts contacts--right">
    <li class="contact">
      <span class="contact__icon"><svg viewBox="0 0 24 24"><path d="M3 5h18a1 1 0 0 1 1 1v12a1 1 0 0 1-1 1H3a1 1 0 0 1-1-1V6a1 1 0 0 1 1-1zm9 7.5L4 7.6V17h16V7.6z"/></svg></span>
      Marc@DorvelEng.com
    </li>
    <li class="contact">
      <span class="contact__icon"><svg viewBox="0 0 24 24"><path d="M12 2a10 10 0 1 0 0 20 10 10 0 0 0 0-20zm6.9 9h-3a15 15 0 0 0-1.4-6 8 8 0 0 1 4.4 6zM12 4c.9 1.2 1.8 3.6 1.9 7h-3.8c.1-3.4 1-5.8 1.9-7zM9.5 5a15 15 0 0 0-1.4 6h-3a8 8 0 0 1 4.4-6zM5.1 13h3a15 15 0 0 0 1.4 6 8 8 0 0 1-4.4-6zM12 20c-.9-1.2-1.8-3.6-1.9-7h3.8c-.1 3.4-1 5.8-1.9 7zm2.5-1a15 15 0 0 0 1.4-6h3a8 8 0 0 1-4.4 6z"/></svg></span>
      www.DorvelEng.com
    </li>
  </ul>
</section>

</body>
</html>
```